Design mobile friendly review and ranking site

We're working on a corporate website for reviewing and ranking fellow employees. We need the website to look both fun and professional and it needs to be responsive - to it works on mobile and desktop.

Looking for css and HTML for 3 key pages as well as a header and footer for the site. Also would need any supporting graphics as part of the design.

Target Market(s)

Professionals in their 20s, 30s, and 40s.

Industry/Entity Type

Internet

Coding

Coded - Design and coding required

Number of Pages Required

3 page

Font styles to use
Sans Serif

Requirements
Must have
• 3 key pages we need (note included screenshots for each - these are just super rough cuts so you see examples of the content.)
• a) main-intro: A compelling into page with a login/registration form. Should be sleek/modern/enticing. Also we would show the ranking for the top 3 people to tease people re: content.
• b) main-page: Has two sections: One at the top where you would rate someone and one at the bottom where it shows a ranking of people.
• c) profile page: This is where you view a specific person. You see the person's picture, some info about the person, you see their overall rating, you can rate them, and you also see their historical ratings.
Nice to have
• Note we need css and HTML for this. It should feel as sleek and modern. Note also must be responsive design so it works well in mobile and desktop.

```html
<!DOCTYPE html>
<html lang="en">
<head>
<meta charset="utf-8">
<title>Team Merit Board – Profile</title>
<link href="https://fonts.googleapis.com/css2?family=Oswald:wght@400&family=Open+Sans:wght@400;600&family=Roboto:wght@400&display=swap" rel="stylesheet">
<style>
:root{
  --page-bg:#ebebeb;
  --panel-bg:#ffffff;
  --panel-border:#d6d6d6;
  --band-top:#fbfbfb;
  --band-bottom:#e4e4e4;
  --brand:#1b7fc4;
  --text:#333333;
  --text-soft:#4a3a3a;
  --star-off:#4b3f40;
  --button:#222222;
  --footer-bg:#2d2e34;
  --footer-text:#ffffff;
  --icon-line:#cfcfcf;
}
*{box-sizing:border-box;margin:0;padding:0}
html,body{width:1110px;height:1200px;overflow:hidden}
body{background:var(--page-bg);font-family:"Open Sans",Arial,sans-serif;color:var(--text);position:relative}

.site-header{position:absolute;left:0;top:0;width:1110px;height:73px;background:linear-gradient(#fafafa,#efefef);border-bottom:1px solid #d8d8d8}
.brand{position:absolute;left:90px;top:18px;font-family:"Oswald",Arial,sans-serif;font-size:25px;color:var(--brand);letter-spacing:.2px;line-height:1.2}
.nav-item{position:absolute;top:0;height:73px;display:flex;align-items:center;font-size:11.5px;color:#333;text-transform:uppercase;gap:7px}
.nav-level{left:356px}
.nav-profile{left:556px}
.nav-logout{left:690px}
.nav-sep{position:absolute;top:0;width:1px;height:73px;background:#dcdcdc}
.search{position:absolute;left:794px;top:18px;width:225px;height:36px;border:1px solid #d4d4d4;border-radius:18px;background:#fff;font-size:10px;color:#555;padding:0 0 0 18px;display:flex;align-items:center}
.search svg{position:absolute;right:14px;top:11px}

.panel{position:absolute;left:90px;width:928px;background:var(--panel-bg);border:1px solid var(--panel-border)}
.panel-title{height:58px;background:linear-gradient(var(--band-top),var(--band-bottom));border-bottom:1px solid #dedede;display:flex;align-items:center;justify-content:center;font-family:"Roboto",Arial,sans-serif;font-size:16.5px;color:#333;text-transform:uppercase;letter-spacing:.2px}
.abs{position:absolute}

.profile{top:122px;height:284px}
.avatar{left:262px;top:103px;width:138px;height:138px;border-radius:50%;border:1px solid #ddd;background:radial-gradient(circle at 50% 40%,#d9b59c 0,#b98a70 35%,#5a3b2c 60%,#e8e8e8 62%,#f2f2f2 100%)}
.profile-meta{left:429px;top:114px;font-size:12.5px;line-height:19px;color:#333}
.rating-row{position:absolute;display:flex;align-items:center;height:20px;font-size:13px;color:#333}
.rating-row .stars{position:absolute}

.stars{display:flex}
.star{display:block}
.star.on{fill:url(#gold);stroke:#c88f00;stroke-width:1}
.star.off{fill:var(--star-off)}
.stars-md .star{width:14px;height:14px;margin-right:4.6px}
.stars-sm .star{width:11px;height:11px;margin-right:3.5px}

.review-form{top:424px;height:364px}
.comment-label{left:307px;top:176px;font-size:11.5px;color:var(--text-soft)}
.comment-box{left:307px;top:198px;width:318px;height:98px;border:1px solid #cfcfcf;border-radius:4px;background:#fff;resize:vertical;font-family:inherit}
.save-btn{left:307px;top:314px;width:69px;height:27px;border:0;border-radius:3px;background:var(--button);color:#fff;font-family:inherit;font-size:11px;text-transform:uppercase}

.history{top:813px;height:231px}
.review-card{position:absolute;top:107px;width:230px}
.review-date{font-size:11.5px;color:#333}

.site-footer{position:absolute;left:0;top:1093px;width:1110px;height:107px;background:var(--footer-bg);color:var(--footer-text);text-align:center}
.copyright{position:absolute;left:0;right:0;top:25px;font-size:10.5px;text-transform:uppercase}
.social{position:absolute;left:492px;top:52px;display:flex;gap:4px}
.social span{width:22px;height:22px;border:1.5px solid var(--icon-line);border-radius:50%}
</style>
</head>
<body>
<svg width="0" height="0" style="position:absolute" aria-hidden="true">
  <defs>
    <linearGradient id="gold" x1="0" y1="0" x2="0" y2="1">
      <stop offset="0" stop-color="#fff07a"/>
      <stop offset="1" stop-color="#f0a500"/>
    </linearGradient>
    <symbol id="star" viewBox="0 0 24 24"><path d="M12 1.5l3.1 6.9 7.4.7-5.6 5 1.7 7.4L12 17.7l-6.6 3.8 1.7-7.4-5.6-5 7.4-.7z"/></symbol>
  </defs>
</svg>

<header class="site-header">
  <div class="brand">TEAM MERIT BOARD</div>
  <div class="nav-item nav-level">Level 3 - 41 points to level 4</div>
  <div class="nav-sep" style="left:540px"></div>
  <div class="nav-item nav-profile">
    <svg width="13" height="13" viewBox="0 0 16 16" fill="#666"><circle cx="8" cy="4.5" r="3.7"/><path d="M1 16c0-4.5 3-7 7-7s7 2.5 7 7z"/></svg>
    Your profile
  </div>
  <div class="nav-sep" style="left:672px"></div>
  <div class="nav-item nav-logout">
    <svg width="12" height="14" viewBox="0 0 12 14" fill="#666"><path d="M3 6V4a3 3 0 0 1 6 0h-1.6a1.4 1.4 0 0 0-2.8 0v2z"/><rect x="0" y="6" width="10" height="8" rx="1"/></svg>
    Log out
  </div>
  <div class="search">Enter Name
    <svg width="13" height="13" viewBox="0 0 14 14" fill="none" stroke="#999" stroke-width="1.6"><circle cx="6" cy="6" r="4.6"/><path d="M9.5 9.5L13 13"/></svg>
  </div>
</header>

<section class="panel profile">
  <h2 class="panel-title">Michael</h2>
  <div class="abs avatar" role="img" aria-label="Portrait photo of Michael"></div>
  <p class="abs profile-meta">Levet 9 in Product Management<br>Reviews: 5 I Score: 4</p>
  <div class="rating-row" style="left:428px;top:164px">Smarts<span class="stars stars-md" style="left:188px">
    <svg class="star on"><use href="#star"/></svg><svg class="star on"><use href="#star"/></svg><svg class="star on"><use href="#star"/></svg><svg class="star off"><use href="#star"/></svg><svg class="star off"><use href="#star"/></svg></span></div>
  <div class="rating-row" style="left:428px;top:189px">Easy to work with<span class="stars stars-md" style="left:188px">
    <svg class="star on"><use href="#star"/></svg><svg class="star on"><use href="#star"/></svg><svg class="star on"><use href="#star"/></svg><svg class="star off"><use href="#star"/></svg><svg class="star off"><use href="#star"/></svg></span></div>
  <div class="rating-row" style="left:428px;top:214px">Hard worker<span class="stars stars-md" style="left:188px">
    <svg class="star on"><use href="#star"/></svg><svg class="star on"><use href="#star"/></svg><svg class="star on"><use href="#star"/></svg><svg class="star off"><use href="#star"/></svg><svg class="star off"><use href="#star"/></svg></span></div>
</section>

<section class="panel review-form">
  <h2 class="panel-title">Update your review for this person:</h2>
  <div class="rating-row" style="left:309px;top:86px">Smarts<span class="stars stars-md" style="left:158px">
    <svg class="star on"><use href="#star"/></svg><svg class="star on"><use href="#star"/></svg><svg class="star on"><use href="#star"/></svg><svg class="star off"><use href="#star"/></svg><svg class="star off"><use href="#star"/></svg></span></div>
  <div class="rating-row" style="left:309px;top:111px">Easy<span class="stars stars-md" style="left:158px">
    <svg class="star on"><use href="#star"/></svg><svg class="star on"><use href="#star"/></svg><svg class="star on"><use href="#star"/></svg><svg class="star off"><use href="#star"/></svg><svg class="star off"><use href="#star"/></svg></span></div>
  <div class="rating-row" style="left:309px;top:136px">Works crazy hard<span class="stars stars-md" style="left:158px">
    <svg class="star on"><use href="#star"/></svg><svg class="star on"><use href="#star"/></svg><svg class="star on"><use href="#star"/></svg><svg class="star off"><use href="#star"/></svg><svg class="star off"><use href="#star"/></svg></span></div>
  <label class="abs comment-label" for="comment">(Optional) Write an anonymous comment about this person:</label>
  <textarea class="abs comment-box" id="comment"></textarea>
  <button class="abs save-btn" type="button">Save</button>
</section>

<section class="panel history">
  <h2 class="panel-title">Reviews for Michael:</h2>
  <div class="review-card" style="left:65px">
    <p class="review-date">Given by a coworker on 2016-04-23</p>
    <div class="rating-row" style="left:0;top:16px">Smarts<span class="stars stars-sm" style="left:143px"><svg class="star on"><use href="#star"/></svg><svg class="star on"><use href="#star"/></svg><svg class="star on"><use href="#star"/></svg><svg class="star off"><use href="#star"/></svg><svg class="star off"><use href="#star"/></svg></span></div>
    <div class="rating-row" style="left:0;top:39px">Easy to work with<span class="stars stars-sm" style="left:143px"><svg class="star on"><use href="#star"/></svg><svg class="star on"><use href="#star"/></svg><svg class="star on"><use href="#star"/></svg><svg class="star off"><use href="#star"/></svg><svg class="star off"><use href="#star"/></svg></span></div>
    <div class="rating-row" style="left:0;top:63px">Hard worker<span class="stars stars-sm" style="left:143px"><svg class="star on"><use href="#star"/></svg><svg class="star on"><use href="#star"/></svg><svg class="star on"><use href="#star"/></svg><svg class="star off"><use href="#star"/></svg><svg class="star off"><use href="#star"/></svg></span></div>
  </div>
  <div class="review-card" style="left:351px">
    <p class="review-date">Given by a coworker on 2016-04-23</p>
    <div class="rating-row" style="left:0;top:16px">Smarts<span class="stars stars-sm" style="left:143px"><svg class="star on"><use href="#star"/></svg><svg class="star on"><use href="#star"/></svg><svg class="star on"><use href="#star"/></svg><svg class="star off"><use href="#star"/></svg><svg class="star off"><use href="#star"/></svg></span></div>
    <div class="rating-row" style="left:0;top:39px">Easy to work with<span class="stars stars-sm" style="left:143px"><svg class="star on"><use href="#star"/></svg><svg class="star on"><use href="#star"/></svg><svg class="star on"><use href="#star"/></svg><svg class="star off"><use href="#star"/></svg><svg class="star off"><use href="#star"/></svg></span></div>
    <div class="rating-row" style="left:0;top:63px">Hard worker<span class="stars stars-sm" style="left:143px"><svg class="star on"><use href="#star"/></svg><svg class="star on"><use href="#star"/></svg><svg class="star on"><use href="#star"/></svg><svg class="star off"><use href="#star"/></svg><svg class="star off"><use href="#star"/></svg></span></div>
  </div>
  <div class="review-card" style="left:644px">
    <p class="review-date">Given by a coworker on 2016-04-23</p>
    <div class="rating-row" style="left:0;top:16px">Smarts<span class="stars stars-sm" style="left:143px"><svg class="star on"><use href="#star"/></svg><svg class="star on"><use href="#star"/></svg><svg class="star on"><use href="#star"/></svg><svg class="star off"><use href="#star"/></svg><svg class="star off"><use href="#star"/></svg></span></div>
    <div class="rating-row" style="left:0;top:39px">Easy to work with<span class="stars stars-sm" style="left:143px"><svg class="star on"><use href="#star"/></svg><svg class="star on"><use href="#star"/></svg><svg class="star on"><use href="#star"/></svg><svg class="star off"><use href="#star"/></svg><svg class="star off"><use href="#star"/></svg></span></div>
    <div class="rating-row" style="left:0;top:63px">Hard worker<span class="stars stars-sm" style="left:143px"><svg class="star on"><use href="#star"/></svg><svg class="star on"><use href="#star"/></svg><svg class="star on"><use href="#star"/></svg><svg class="star off"><use href="#star"/></svg><svg class="star off"><use href="#star"/></svg></span></div>
  </div>
</section>

<footer class="site-footer">
  <p class="copyright">©2016 &nbsp;Team Merit Board., all rights reserved.</p>
  <div class="social" aria-label="Social links"><span></span><span></span><span></span><span></span><span></span></div>
</footer>
</body>
</html>
```